Flyer-Design für Dekorations- und Farbkonzepte
hat alles bestens geklappt und tolles Design...kann Sie nur weiterempfehlen! PS. Lieben Dank für die Geduld! Beste Grüsse Rosalie Trachsler
Zielgruppe
Dekorationskonzepte, Farbkonzepte für Räume, Planung und Realisation Geschäfts - und Privatkunden, Zielgruppe Firmen, Seniorenheime , Privatkundschaft
Aufgabenstellung
Ich bin im Mai an einem Anlass in einem Seniorenheim und habe die Möglichkeit mich zu präsentieren , ich mache an diesem Anlass die Dekoration und möchte dabei Tag einen wertigen Flyer abgeben. An diesem Anlass sind auch der Gemeindepräsident und Angehörige der Bewohner etc . eingeladen. Der Flyer soll etwas gediegen daherkommen und über meine Arbeit informieren. Ich möchte vorallem Geschäftskunden ansprechen. Der Flyer sollte Emotionen wecken. Masse ca. A5 ..bin da sehr offen (nicht zu klein )

```html
<!DOCTYPE html>
<html lang="de">
<head>
<meta charset="utf-8">
<title>Dienstleistungen – Farbkonzepte und Raumgestaltung</title>
<link rel="stylesheet" href="https://fonts.googleapis.com/css2?family=Antonio:wght@100;200&family=Yanone+Kaffeesatz:wght@300&display=swap">
<style>
  :root {
    --paper: #ffffff;
    --slate: #7b8ea3;
    --ink: #ffffff;
    --photo-light: #e4e2df;
    --photo-warm: #e9c9b8;
    --photo-dark: #6b5548;
  }
  * { margin: 0; padding: 0; box-sizing: border-box; }
  html, body {
    width: 846px; height: 1200px; overflow: hidden;
    background: var(--paper);
  }
  .flyer { position: relative; width: 846px; height: 1200px; }
  .panel {
    position: absolute;
    left: 29px; top: 29px; width: 787px; height: 1140px;
    background: var(--slate);
    color: var(--ink);
  }
  .page-title {
    position: absolute; left: 47px; top: 40px;
    font-family: "Antonio", sans-serif; font-weight: 100;
    font-size: 58px; letter-spacing: 4px; line-height: 1;
    white-space: nowrap;
  }
  .service-title {
    position: absolute; top: 130px;
    font-family: "Antonio", sans-serif; font-weight: 100;
    font-size: 36px; letter-spacing: 4px; line-height: 1;
    white-space: nowrap;
  }
  .service-title--colour { left: 47px; }
  .service-title--space { left: 395px; }
  .service-body {
    position: absolute; top: 193px; width: 340px;
    font-family: "Yanone Kaffeesatz", sans-serif; font-weight: 300;
    font-size: 29px; line-height: 34px;
  }
  .service-body--colour { left: 47px; }
  .service-body--space { left: 395px; }
  .service-list { list-style: none; }
  .service-list li { position: relative; padding-left: 37px; white-space: nowrap; }
  .service-list li::before {
    content: ""; position: absolute; left: 2px; top: 15px;
    width: 4px; height: 4px; background: var(--ink);
  }
  .rule {
    position: absolute; left: 47px; width: 696px; height: 2px;
    background: var(--ink);
  }
  .rule--top { top: 421px; }
  .rule--bottom { top: 674px; }
  .motto {
    position: absolute; left: 0; top: 445px; width: 787px;
    text-align: center;
    font-family: "Antonio", sans-serif; font-weight: 100;
    font-size: 54px; letter-spacing: 4px; line-height: 70.5px;
  }
  .motto-line { display: block; white-space: nowrap; }
  .photo {
    position: absolute; left: 87px; top: 722px; width: 612px; height: 301px;
    background: linear-gradient(100deg, var(--photo-dark) 0%, var(--photo-light) 22%, var(--photo-light) 60%, var(--photo-warm) 85%);
  }
</style>
</head>
<body>
<div class="flyer">
  <section class="panel">
    <h1 class="page-title">DIENSTLEISTUNGEN</h1>

    <h2 class="service-title service-title--colour">FARBKONZEPTE</h2>
    <div class="service-body service-body--colour">
      <ul class="service-list">
        <li>Bedarfsermittlung</li>
        <li>Farbkonzept mit Moodboard</li>
        <li>Auswahl passender Möbel, Texti-<br>lien und Accessoires</li>
      </ul>
    </div>

    <h2 class="service-title service-title--space">RAUMGESTALTUNG</h2>
    <div class="service-body service-body--space">
      <p class="service-intro">unter Anderem:</p>
      <ul class="service-list">
        <li>Konzeptidee</li>
        <li>Umsetzungsplan</li>
        <li>Beleuchtungskonzept</li>
        <li>Zielgruppenanalyse</li>
      </ul>
    </div>

    <div class="rule rule--top"></div>
    <p class="motto">
      <span class="motto-line">„WENN MENSCH UND RAUM</span>
      <span class="motto-line">ZUSAMMENPASSEN, ENTSTEHT</span>
      <span class="motto-line">HARMONIE.“</span>
    </p>
    <div class="rule rule--bottom"></div>

    <div class="photo" role="img" aria-label="Foto: Grundrisspläne mit Holzmustern, Lederproben und einem rosa Farbfächer"></div>
  </section>
</div>
</body>
</html>
```